Peanut Butter - Single Serve Sachet

We are a sports and wellness nutrition company (https://www.brightkelpfoods.in) and launching a new product Peanut Butter. Need attractive design of single serve sachet.

The product should be unique and eye catchy. It should have enough space to mention USPs later.

The product USP is tear-on the go sachet, image mockup has been attached.

Target Market(s)

Sports Persons and General Public looking for Peanut Butter.

Industry/Entity Type

Nutrition

Colors

Designer to choose colors to be used in the design.

Requirements
Must have
• Single serve sachet design. Attractive colour theme with Peanut Butter mentioned as bold.
Should not have
• no black colour

Files

```html
<!DOCTYPE html>
<html lang="en">
<head>
<meta charset="utf-8">
<title>Brightkelp Foods – Peanut Butter Sachet</title>
<link href="https://fonts.googleapis.com/css2?family=Pacifico&family=Roboto:wght@400;500;700&display=swap" rel="stylesheet">
<style>
  :root {
    --backdrop: #d0d0cf;
    --sachet-orange: #f7a21f;
    --sachet-tan: #d8a95e;
    --cream: #fbf4b4;
    --brown: #4b2412;
  }
  html, body {
    margin: 0;
    padding: 0;
    width: 1200px;
    height: 1200px;
    overflow: hidden;
    background: var(--backdrop);
  }
  .canvas {
    display: block;
    width: 1200px;
    height: 1200px;
  }
  .sachet-body { fill: var(--sachet-orange); }
  .sachet-panel { fill: var(--sachet-tan); }
  .brand-name {
    font-family: "Roboto", sans-serif;
    font-weight: 700;
    font-size: 19px;
    fill: var(--brown);
  }
  .brand-mark { fill: var(--brown); }
  .brand-rule { stroke: var(--brown); stroke-width: 1; }
  .brand-tagline {
    font-family: "Roboto", sans-serif;
    font-weight: 500;
    font-size: 7.5px;
    letter-spacing: 2.4px;
    fill: var(--brown);
  }
  .title {
    font-family: "Pacifico", cursive;
  }
  .title-peanut { fill: var(--cream); font-size: 104px; }
  .title-butter { fill: var(--brown); font-size: 112px; }
  .facts {
    font-family: "Roboto", sans-serif;
    font-size: 12.5px;
    fill: var(--brown);
  }
  .facts-value { text-anchor: end; }
  .net-label {
    font-family: "Roboto", sans-serif;
    font-weight: 700;
    font-size: 9.5px;
    fill: var(--brown);
  }
  .net-value {
    font-family: "Roboto", sans-serif;
    font-weight: 700;
    font-size: 14px;
    fill: var(--brown);
  }
</style>
</head>
<body>
<svg class="canvas" viewBox="0 0 1200 1200" xmlns="http://www.w3.org/2000/svg">
  <defs>
    <clipPath id="sachet-shape">
      <path d="M520 165 H682 Q694 165 694 177 V244 Q686 246 686 251 Q686 256 694 258 V330 L806 412 V1018 Q806 1040 784 1040 H416 Q394 1040 394 1018 V412 L508 330 V258 Q516 256 516 251 Q516 246 508 244 V177 Q508 165 520 165 Z"/>
    </clipPath>
  </defs>

  <g class="sachet" clip-path="url(#sachet-shape)">
    <rect class="sachet-body" x="380" y="150" width="440" height="900"/>
    <path class="sachet-panel" d="M806 418 C700 430 628 520 620 640 C614 720 640 770 612 825 C568 905 512 960 506 1040 L806 1040 Z"/>
  </g>

  <g class="brand">
    <circle class="brand-mark" cx="482" cy="415" r="6"/>
    <text class="brand-name" x="600" y="422" text-anchor="middle">Brightkelp FOODS</text>
    <line class="brand-rule" x1="484" y1="430" x2="705" y2="430"/>
    <text class="brand-tagline" x="594" y="442" text-anchor="middle">PREMIUM SPORTS NUTRITION</text>
  </g>

  <g class="title">
    <text class="title-peanut" x="422" y="652" textLength="364" lengthAdjust="spacingAndGlyphs">Peanut</text>
    <text class="title-butter" x="410" y="755" textLength="346" lengthAdjust="spacingAndGlyphs">Butter</text>
  </g>

  <g class="facts">
    <text x="427" y="901">Nutritition A</text>
    <text x="427" y="917">Nutrition B</text>
    <text x="427" y="932">Vitamin</text>
    <text x="427" y="948">No Added Artificial Colours, Flavours,</text>
    <text x="427" y="963">Presevatives or Thickerners</text>
    <text class="facts-value" x="776" y="901">13.9 g</text>
    <text class="facts-value" x="776" y="917">7.9 g</text>
    <text class="facts-value" x="776" y="932">8.0 g</text>
    <text class="facts-value" x="776" y="948">9.0 g</text>
  </g>

  <text x="779" y="998" text-anchor="end"><tspan class="net-label">Netto: </tspan><tspan class="net-value">40 g</tspan></text>
</svg>
</body>
</html>
```